Easy Marinade Labels for Butchery Store

Need a set of labels designed for a Butchery Shop. They will sit in the top left corner of the packets as a triangle (7cm each side). Easy because the only major requirement is the label name and some small text saying "Please ask in store to see spec sheet for ingredients". Extra points for finding a fun way to incorporate the logo and/or images of food (garlic bulbs, chilli, spices ect) to enhance the label. List of Marinade Names below: GarlicPepper Mint & RosemarySatayBBQChilli Plum & GingerSundried Tomato & BasilBuffaloHoney SoyHoi-SinPer PeriSpicy CajunTeriyakiBlack Bean Ive also attached the logo and an example of how the label might sit on a packet of meat. Thanks

Target Market(s)

Butchery Deli Shop Customers

Industry/Entity Type

Food Store

Font styles to use
Serif
Sans Serif
Decorative
Other font styles liked:
• Fun font that isn't a generic Quillbrenn Font?

Colors

Designer to choose colors to be used in the design.

Requirements
Must have
• Product Name
• Small text saying "Please ask in store to see spec sheet for ingredients"
Nice to have
• Photos of ingredients that would match that type of marinade - Chilli, Garlic, Spices.
• Tavo Crest Logo - not essential if it doesn't look good on the label / doesn't fit.

```html
<!DOCTYPE html>
<html lang="en">
<head>
<meta charset="utf-8">
<title>Tavo Crest – Marinade Corner Label</title>
<link href="https://fonts.googleapis.com/css2?family=Barlow+Condensed:wght@700;800&display=swap" rel="stylesheet">
<style>
  :root {
    --paper: #ffffff;
    --slate: #1d2228;
    --slate-deep: #14181d;
    --spice: #b3120c;
    --spice-glow: #d3200f;
    --label-text: #ffffff;
  }
  html, body {
    margin: 0;
    padding: 0;
    width: 1200px;
    height: 1200px;
    overflow: hidden;
    background: var(--paper);
  }
  .label-canvas {
    display: block;
    width: 1200px;
    height: 1200px;
  }
  .product-name {
    font-family: "Barlow Condensed", "Arial Narrow", sans-serif;
    font-weight: 800;
    font-size: 186px;
    fill: var(--label-text);
    letter-spacing: 2px;
  }
  .ingredients-note {
    font-family: "Barlow Condensed", "Arial Narrow", sans-serif;
    font-weight: 700;
    font-size: 50px;
    fill: var(--label-text);
  }
</style>
</head>
<body>
<svg class="label-canvas" viewBox="0 0 1200 1200" xmlns="http://www.w3.org/2000/svg">
  <defs>
    <radialGradient id="spice-dust" cx="0.34" cy="0.32" r="0.42">
      <stop offset="0" stop-color="var(--spice-glow)"/>
      <stop offset="0.35" stop-color="var(--spice)"/>
      <stop offset="0.75" stop-color="#4a1614"/>
      <stop offset="1" stop-color="var(--slate)"/>
    </radialGradient>
    <linearGradient id="slate-shade" x1="0" y1="0" x2="1" y2="1">
      <stop offset="0" stop-color="var(--slate-deep)" stop-opacity="0"/>
      <stop offset="1" stop-color="var(--slate-deep)" stop-opacity="0.6"/>
    </linearGradient>
  </defs>

  <g class="label-photo" role="img" aria-label="Photo of red chilli powder, chilli flakes and a sliced red chilli on dark slate">
    <polygon points="0,0 1200,0 0,1200" fill="url(#spice-dust)"/>
    <polygon points="0,0 1200,0 0,1200" fill="url(#slate-shade)"/>
  </g>

  <text class="product-name" x="187" y="727" transform="rotate(-45 187 727)" textLength="730" lengthAdjust="spacingAndGlyphs">TAVO CREST</text>

  <text class="ingredients-note" x="144" y="958" transform="rotate(-45 144 958)" textLength="1123" lengthAdjust="spacingAndGlyphs">PLEASE ASK IN STORE TO SEE SPEC SHEET FOR INGREDIENTS</text>
</svg>
</body>
</html>
```